business card with 2 locations on 1 card

I need a modern looking business card that I would use at 2 different locations. Possibly 1 location on 1 side and other location on other side. One should be able to distinguish the 2 locations immediately before having to read the address or description on card. You can take a look at my website to see what I'm drawn to. The logo is brand new that I just purchased on Craft Hive. I want to emphasize family.
Updates

Let's not use the yellow and blue colors. Added Thursday, August 31, 2017

Target Market(s)

women and children

Industry/Entity Type

Health And Wellness

Contact Information for Business Card

Business name: Willow Brook Chiropractic & Acupuncture
My name: Lorin Daske
Job title: DC, MSOM, LAC (NV), CCN

Location 1
Address: 4817 Marlowe Blvd, Suite C-210, Ashbury, TX 75561
Phone: (469) 555-0182
Fax: (972) 555-0137

Location 2
Address: 1936 Belvane Road, Suite 340, Denmore, TX 75587
Phone: (469) 555-0169
Fax: (972) 555-0137

Email: drlorindaske@mailnest.example
Website: www.drlorindaske.example

Font styles to use
Serif
Sans Serif

Colors

Designer to choose colors to be used in the design.

Requirements
Must have
• distinction between 2 locations.
Nice to have
• Colors preference below is there. But I like to see what you come up with too!

```html
<!DOCTYPE html>
<html lang="en">
<head>
<meta charset="utf-8">
<title>Willow Brook Chiropractic &amp; Acupuncture – Business Cards</title>
<link rel="stylesheet" href="https://fonts.googleapis.com/css2?family=Cinzel:wght@400;500&family=Source+Sans+3:wght@400;700&display=swap">
<style>
  :root {
    --backdrop: #e8e4de;
    --card-white: #ffffff;
    --teal: #2a6d6d;
    --leaf-green: #2f9a2f;
    --card-green: #0a8a1f;
    --ink: #444444;
    --on-green: #ffffff;
  }
  * { margin: 0; padding: 0; box-sizing: border-box; }
  html, body { width: 1200px; height: 960px; overflow: hidden; }
  body {
    position: relative;
    background: var(--backdrop);
    font-family: "Source Sans 3", "Myriad Pro", Arial, sans-serif;
  }
  .card {
    position: absolute;
    width: 600px;
    height: 344px;
    box-shadow: 0 3px 8px rgba(0,0,0,.28);
  }
  /* first location side */
  .card-west { left: 314px; top: 113px; background: var(--card-white); }
  .brand-mark { position: absolute; border-radius: 50%; }
  .card-west .brand-mark {
    left: 64px; top: 26px; width: 106px; height: 106px;
    border: 6px solid var(--teal);
  }
  .brand-name {
    position: absolute;
    font-family: "Cinzel", "Trajan Pro", Georgia, serif;
    font-weight: 500;
    line-height: 1;
    white-space: nowrap;
  }
  .brand-name .brand-title { display: block; }
  .brand-name .brand-sub { display: block; }
  .card-west .brand-name { left: 25px; top: 143px; color: var(--teal); }
  .card-west .brand-title { font-size: 25px; }
  .card-west .brand-sub { font-size: 11.5px; margin-top: 3px; letter-spacing: .1px; }
  .contact-list {
    position: absolute;
    left: 25px; top: 192px;
    list-style: none;
    color: var(--ink);
    font-size: 15px;
    line-height: 19.5px;
  }
  .contact-list li { display: flex; align-items: center; gap: 6px; }
  .contact-list svg { width: 14px; height: 12px; fill: var(--teal); flex: none; }
  .contact-list .email { margin-top: 2px; }
  .doctor {
    position: absolute;
    right: 31px; top: 220px;
    text-align: right;
  }
  .doctor-name { color: var(--teal); font-weight: 700; font-size: 22px; line-height: 26px; letter-spacing: .3px; }
  .doctor-title { color: var(--leaf-green); font-size: 16px; line-height: 20px; letter-spacing: .3px; }
  .accent-dot {
    position: absolute;
    left: 483px; top: 272px; width: 40px; height: 40px;
    border-radius: 50%;
    background: var(--leaf-green);
  }
  .web-band {
    position: absolute;
    left: 0; bottom: 0; width: 100%; height: 24px;
    background: var(--teal);
    color: var(--on-green);
    font-size: 15px;
    letter-spacing: 3.2px;
    line-height: 24px;
    padding-left: 29px;
  }
  /* second location side */
  .card-east { left: 312px; top: 472px; background: var(--card-green); color: var(--on-green); text-align: center; }
  .card-east .brand-mark {
    left: 232px; top: 50px; width: 130px; height: 130px;
    background: var(--on-green);
  }
  .card-east .brand-name { left: 0; width: 100%; top: 193px; color: var(--on-green); }
  .card-east .brand-title { font-size: 29px; }
  .card-east .brand-sub { font-size: 13px; margin-top: 3px; }
  .location-contact {
    position: absolute;
    left: 0; width: 100%; top: 246px;
    font-size: 15px;
    line-height: 26px;
  }
</style>
</head>
<body>

<section class="card card-west" aria-label="Denmore location card">
  <div class="brand-mark" aria-hidden="true"></div>
  <div class="brand-name">
    <span class="brand-title">Willow Brook</span>
    <span class="brand-sub">Chiropractic &amp; Acupuncture</span>
  </div>
  <ul class="contact-list">
    <li>1936 Belvane Road</li>
    <li>Suite 340, Denmore, TX 75587</li>
    <li><svg viewBox="0 0 14 12" aria-hidden="true"><path d="M1 3c0-2 2-2.5 6-2.5S13 1 13 3v1.5h-3V3H4v1.5H1z"/><path d="M3 5h8l2 6H1z"/><circle cx="7" cy="8" r="1.6" fill="#fff"/></svg>(469) 555-0169</li>
    <li><svg viewBox="0 0 14 12" aria-hidden="true"><rect x="3" y="0" width="8" height="4"/><rect x="0" y="4" width="14" height="6" rx="1"/><rect x="3" y="8" width="8" height="4"/></svg>(972) 555-0137</li>
    <li class="email"><svg viewBox="0 0 14 12" aria-hidden="true"><rect x="0" y="2" width="14" height="9"/><path d="M0 2l7 5 7-5" stroke="#fff" stroke-width="1.2" fill="none"/></svg>drlorindaske@mailnest.example</li>
  </ul>
  <div class="doctor">
    <p class="doctor-name">LORIN DASKE</p>
    <p class="doctor-title">DC, MSOM, LAC (NV), CCN</p>
  </div>
  <div class="accent-dot" aria-hidden="true"></div>
  <p class="web-band">www.drlorindaske.example</p>
</section>

<section class="card card-east" aria-label="Ashbury location card">
  <div class="brand-mark" aria-hidden="true"></div>
  <div class="brand-name">
    <span class="brand-title">Willow Brook</span>
    <span class="brand-sub">Chiropractic &amp; Acupuncture</span>
  </div>
  <div class="location-contact">
    <p>P : (469) 555-0182&nbsp;&nbsp;F : (972) 555-0137</p>
    <p>4817 Marlowe Blvd, Suite C-210, Ashbury, TX 75561</p>
  </div>
</section>

</body>
</html>
```